Velora Pedalworks

We are a new start up company selling (online) innovative cycling products.
Being a new player in the market a modern eye catching logo would be good.
Initially selling safety tail lights with blinkers & modern designed cycling gloves and eventually extending our range into cycling clothing. Many of our products will have a safety theme.

Please see logo attached.

Reason: I have extended deadline because i have just received the Logo to be used.

Target Market(s)

We will be target marketing to the young 20-30year old trendy commuter cyclists to the 40 - 60 year old weekend road riders with there immaculate color coordinated road bikes & clothing.

Industry/Entity Type

Safety

Requirements
Must have
• Name: Mavin Tolby
Line for Mobile No. 0438 261 905
Line for email Address: mavin@velorapedalworks.example.com.au
3 Lines for Postal Address: PO Box 3862
Wattle Crest Corner
NSW 2174
Website: www.velorapedalworks.example.com.au

```html
<!DOCTYPE html>
<html lang="en">
<head>
<meta charset="utf-8">
<title>Mavin Tolby – Velora Pedalworks Business Card</title>
<link rel="stylesheet" href="https://fonts.googleapis.com/css2?family=Open+Sans:wght@400;700&family=Roboto+Condensed:wght@400&display=swap">
<style>
  :root {
    --backdrop: #0d0d0d;
    --orange: #ee7623;
    --charcoal: #2d2d2d;
    --stripe: #1e1e1e;
    --paper: #ffffff;
    --ink: #111111;
    --logo-ink: #222222;
    --title-grey: #dcdcdc;
  }
  * { margin: 0; padding: 0; box-sizing: border-box; }
  html, body {
    width: 1200px; height: 900px; overflow: hidden;
    background: var(--backdrop);
  }
  .business-card {
    position: absolute; left: 122px; top: 165px;
    width: 956px; height: 574px;
    background: var(--paper);
    overflow: hidden;
  }
  .header-shapes { position: absolute; left: 0; top: 0; width: 956px; height: 140px; }
  .header-orange { fill: var(--orange); }
  .header-charcoal { fill: var(--charcoal); }
  .person-name {
    position: absolute; left: 87px; top: 64px;
    font-family: "Open Sans", sans-serif; font-weight: 400;
    font-size: 38px; color: var(--paper); letter-spacing: -0.5px;
    text-transform: uppercase;
  }
  .person-title {
    position: absolute; left: 601px; top: 75px;
    font-family: "Roboto Condensed", sans-serif;
    font-size: 26px; color: var(--title-grey);
  }
  .brand-name {
    position: absolute; left: 60px; top: 335px; width: 430px;
    text-align: center;
    font-family: "Open Sans", sans-serif; font-weight: 700;
    font-size: 40px; color: var(--logo-ink); letter-spacing: -0.5px;
  }
  .contact-list { position: absolute; left: 504px; top: 237px; list-style: none; }
  .contact-item {
    display: flex; align-items: center; height: 32px; margin-bottom: 12.5px;
    font-family: "Roboto Condensed", sans-serif; font-size: 20px; color: var(--ink);
  }
  .contact-icon { width: 32px; height: 32px; margin-right: 13px; flex: none; }
  .contact-icon circle { fill: var(--orange); }
  .contact-icon .glyph { fill: var(--paper); }
  .contact-icon .glyph-line { fill: none; stroke: var(--paper); stroke-width: 2; stroke-linecap: round; }
  .footer-stripe { position: absolute; left: 0; top: 493px; width: 956px; height: 17px; background: var(--stripe); }
  .footer-band { position: absolute; left: 0; top: 510px; width: 956px; height: 64px; background: var(--orange); }
</style>
</head>
<body>
  <div class="business-card">
    <svg class="header-shapes" viewBox="0 0 956 140" aria-hidden="true">
      <path class="header-charcoal" d="M520 118 C545 90 555 64 605 64 H956 V118 Z"/>
      <path class="header-orange" d="M0 0 H956 V64 H605 C555 64 545 90 520 118 C505 132 495 140 465 140 H0 Z"/>
    </svg>
    <h1 class="person-name">Mavin Tolby</h1>
    <p class="person-title">Managing Director</p>

    <p class="brand-name">Velora Pedalworks</p>

    <ul class="contact-list">
      <li class="contact-item">
        <svg class="contact-icon" viewBox="0 0 32 32" aria-hidden="true">
          <circle cx="16" cy="16" r="16"/>
          <path class="glyph" d="M16 7 a6 6 0 0 1 6 6 c0 4.5 -6 12 -6 12 s-6 -7.5 -6 -12 a6 6 0 0 1 6 -6 z"/>
          <circle cx="16" cy="13" r="2.2" style="fill:var(--orange)"/>
        </svg>
        PO Box 3862, Wattle Crest Corner , NSW 2174
      </li>
      <li class="contact-item">
        <svg class="contact-icon" viewBox="0 0 32 32" aria-hidden="true">
          <circle cx="16" cy="16" r="16"/>
          <rect class="glyph" x="11" y="7" width="10" height="18" rx="1.5"/>
          <rect x="12.8" y="9" width="6.4" height="5" style="fill:var(--orange)"/>
          <g style="fill:var(--orange)">
            <rect x="12.8" y="16" width="1.6" height="1.6"/><rect x="15.2" y="16" width="1.6" height="1.6"/><rect x="17.6" y="16" width="1.6" height="1.6"/>
            <rect x="12.8" y="19" width="1.6" height="1.6"/><rect x="15.2" y="19" width="1.6" height="1.6"/><rect x="17.6" y="19" width="1.6" height="1.6"/>
          </g>
        </svg>
        0438 261 905
      </li>
      <li class="contact-item">
        <svg class="contact-icon" viewBox="0 0 32 32" aria-hidden="true">
          <circle cx="16" cy="16" r="16"/>
          <rect class="glyph" x="7" y="10" width="18" height="12"/>
          <path d="M7.5 10.5 L16 17 L24.5 10.5 M7.5 21.5 L13.5 15.5 M24.5 21.5 L18.5 15.5" style="fill:none;stroke:var(--orange);stroke-width:1.2"/>
        </svg>
        mavin@velorapedalworks.example.com.au
      </li>
      <li class="contact-item">
        <svg class="contact-icon" viewBox="0 0 32 32" aria-hidden="true">
          <circle cx="16" cy="16" r="16"/>
          <rect class="glyph-line" x="14" y="8" width="6" height="10" rx="3" transform="rotate(45 17 13)"/>
          <rect class="glyph-line" x="12" y="14" width="6" height="10" rx="3" transform="rotate(45 15 19)"/>
        </svg>
        www.velorapedalworks.example.com.au
      </li>
    </ul>

    <div class="footer-stripe"></div>
    <div class="footer-band"></div>
  </div>
</body>
</html>
```